Kestrel Builders Business Card Design Project

Clean sharp business card
Ability to write on back of card
Details for the card -
Address: PO Box 5867, Tarrowin, Qld, 4186
ABN: 47 305 961 220
BSA LIC 2650874
Ph: 07 3562 4470
Fax: 07 3562 4475
Email: kestrelbuilders@mailbrook.com.au

```html
<!DOCTYPE html>
<html lang="en">
<head>
<meta charset="utf-8">
<title>Kestrel Builders – Business Card</title>
<link rel="stylesheet" href="https://fonts.googleapis.com/css2?family=Lato:wght@400;700;900&display=swap">
<style>
  :root {
    --canvas-bg: #d9d9d9;
    --card-white: #ffffff;
    --band-dark: #2b2b2b;
    --accent-orange: #f28a1a;
    --logo-grey: #8c8e91;
    --ink-black: #111111;
    --rule-grey: #8f8f8f;
    --divider: #555555;
  }
  * { box-sizing: border-box; margin: 0; padding: 0; }
  html, body {
    width: 1200px; height: 900px; overflow: hidden;
    background: var(--canvas-bg);
    font-family: "Lato", Arial, sans-serif;
  }
  .canvas {
    width: 1200px; height: 900px;
    display: flex; align-items: center; justify-content: center; gap: 40px;
  }
  .card {
    width: 540px; height: 330px;
    background: var(--card-white);
    position: relative;
    overflow: hidden;
    box-shadow: 0 6px 18px rgba(0,0,0,0.18);
  }

  /* Back: notes side */
  .card-back { padding: 30px 34px 26px; }
  .notes-title {
    font-weight: 900; font-size: 22px; letter-spacing: 1px;
    color: var(--ink-black);
  }
  .notes-lines { list-style: none; margin-top: 4px; }
  .notes-lines li {
    height: 32px;
    border-bottom: 1.5px solid var(--rule-grey);
  }
  .notes-lines li:first-child { margin-left: 130px; height: 4px; }

  /* Front: brand and details */
  .brand-area {
    height: 190px;
    display: flex; align-items: center; justify-content: center; gap: 14px;
  }
  .brand-dot {
    width: 22px; height: 22px; border-radius: 50%;
    background: var(--accent-orange);
  }
  .brand-name {
    font-weight: 700; font-size: 40px; letter-spacing: 1px;
    color: var(--logo-grey);
  }
  .details-band {
    position: absolute; left: 0; right: 0; top: 190px; height: 110px;
    background: var(--band-dark);
    display: flex; padding: 14px 20px;
  }
  .details-col { font-weight: 700; line-height: 1.35; color: #fff; white-space: nowrap; }
  .details-col.address { flex: 0 0 262px; padding-right: 14px; font-size: 14.5px; }
  .details-col.contact {
    flex: 1; padding-left: 16px; font-size: 12.5px;
    border-left: 1px solid var(--divider);
    display: flex; flex-direction: column; justify-content: space-around;
  }
  .label { color: var(--accent-orange); }
  .details-col.address .group + .group { margin-top: 8px; }
  .details-col.contact .value { font-weight: 400; }
</style>
</head>
<body>
<main class="canvas">
  <section class="card card-back" aria-label="Card back, notes">
    <h2 class="notes-title">NOTES:</h2>
    <ul class="notes-lines">
      <li></li><li></li><li></li><li></li><li></li><li></li><li></li><li></li>
    </ul>
  </section>

  <section class="card card-front" aria-label="Card front">
    <div class="brand-area">
      <span class="brand-dot"></span>
      <h1 class="brand-name">Kestrel Builders</h1>
    </div>
    <div class="details-band">
      <div class="details-col address">
        <div class="group">
          <div class="label">Address:</div>
          <div class="value">PO Box 5867, Tarrowin, Qld, 4186</div>
        </div>
        <div class="group">
          <div><span class="label">ABN:</span> 47 305 961 220</div>
          <div>BAS LIC 2650874</div>
        </div>
      </div>
      <div class="details-col contact">
        <div><span class="label">Ph:</span> <span class="value">07 3562 4470</span></div>
        <div><span class="label">Fax:</span> <span class="value">07 3562 4475</span></div>
        <div><span class="label">Email:</span> <span class="value">kestrelbuilders@mailbrook.com.au</span></div>
      </div>
    </div>
  </section>
</main>
</body>
</html>
```